The Bright Socket Business cards

one side I would like my logo (uploaded) and the other side I want my details. I'm an electrician in sydney. The logo side I'm happy with just a white background and our logo in the middle.

Details for other side
24/7 Sydney Electrician
Marcus Hale
0431 758 216
marcus@thebrightsocket.com.au
thebrightsocket.com.au
icons for facebook, instagram, linked in

electrician

company info

```html
<!DOCTYPE html>
<html lang="en">
<head>
<meta charset="utf-8">
<title>The Bright Socket – Business Cards</title>
<link href="https://fonts.googleapis.com/css2?family=Michroma&family=Quicksand:wght@500&display=swap" rel="stylesheet">
<style>
  :root {
    --backdrop: #2b2b2b;
    --card: #ffffff;
    --red: #e8311f;
    --ink: #141414;
    --rule: #9a9a9a;
    --muted: #f1f1f1;
  }
  * { box-sizing: border-box; margin: 0; padding: 0; }
  html, body { width: 1200px; height: 1108px; overflow: hidden; }
  body {
    background: var(--backdrop);
    display: flex;
    justify-content: center;
    align-items: center;
    gap: 70px;
  }
  .card {
    width: 360px;
    height: 600px;
    background: var(--card);
    border-radius: 22px;
    position: relative;
    overflow: hidden;
    display: flex;
    flex-direction: column;
    align-items: center;
  }
  .wordmark {
    font-family: "Michroma", sans-serif;
    color: var(--red);
    font-size: 30px;
    line-height: 1.25;
    text-transform: uppercase;
    text-align: center;
    letter-spacing: 1px;
  }
  /* details side */
  .card--details .wordmark { margin-top: 90px; }
  .holder-name {
    font-family: "Michroma", sans-serif;
    color: var(--red);
    font-size: 21px;
    letter-spacing: 1px;
    text-transform: uppercase;
    margin-top: 175px;
  }
  .contact-rule {
    display: flex;
    align-items: center;
    gap: 8px;
    width: 270px;
    margin-top: 14px;
  }
  .contact-rule::before, .contact-rule::after {
    content: "";
    flex: 1;
    height: 1px;
    background: var(--rule);
  }
  .contact-icon {
    width: 26px; height: 26px;
    background: var(--red);
    border-radius: 5px;
    display: flex; align-items: center; justify-content: center;
  }
  .contact-list {
    list-style: none;
    font-family: "Quicksand", sans-serif;
    font-weight: 500;
    color: var(--ink);
    font-size: 16px;
    line-height: 1.45;
    text-align: center;
    margin-top: 10px;
  }
  .divider {
    width: 270px; height: 1px;
    background: var(--rule);
    margin-top: 14px;
  }
  .tagline {
    font-family: "Michroma", sans-serif;
    font-size: 15px;
    color: var(--ink);
    text-transform: uppercase;
    margin-top: 16px;
    letter-spacing: 0.5px;
  }
  .tagline__hours { color: var(--red); }
  /* logo side */
  .card--logo { justify-content: center; }
  .card--logo .texture {
    position: absolute; inset: 0;
    background: linear-gradient(160deg, var(--muted), #ffffff 55%, var(--muted));
  }
  .card--logo .wordmark { position: relative; margin-top: 40px; }
  .social-links {
    position: absolute;
    bottom: 70px;
    left: 50%;
    transform: translateX(-50%);
    display: flex;
    gap: 10px;
  }
  .social-links span {
    width: 30px; height: 30px;
    border: 1.5px solid var(--red);
    border-radius: 50%;
  }
</style>
</head>
<body>
  <section class="card card--details" aria-label="Contact side">
    <div class="wordmark">The Bright<br>Socket</div>
    <h1 class="holder-name">Marcus Hale</h1>
    <div class="contact-rule">
      <span class="contact-icon">
        <svg width="16" height="16" viewBox="0 0 24 24" fill="#fff" aria-label="Phone"><path d="M6.6 10.8a15 15 0 0 0 6.6 6.6l2.2-2.2a1 1 0 0 1 1-.25 11 11 0 0 0 3.6.6 1 1 0 0 1 1 1V20a1 1 0 0 1-1 1A17 17 0 0 1 3 4a1 1 0 0 1 1-1h3.5a1 1 0 0 1 1 1 11 11 0 0 0 .6 3.6 1 1 0 0 1-.25 1z"/></svg>
      </span>
      <span class="contact-icon">
        <svg width="16" height="16" viewBox="0 0 24 24" fill="none" stroke="#fff" stroke-width="2" aria-label="Email"><rect x="3" y="5" width="18" height="14" rx="1"/><path d="M3 6l9 7 9-7"/></svg>
      </span>
      <span class="contact-icon">
        <svg width="16" height="16" viewBox="0 0 24 24" fill="none" stroke="#fff" stroke-width="2" aria-label="Website"><circle cx="12" cy="12" r="9"/><path d="M3 12h18M12 3c3 3 3 15 0 18M12 3c-3 3-3 15 0 18"/></svg>
      </span>
    </div>
    <ul class="contact-list">
      <li>0431 758 216</li>
      <li>marcus@thebrightsocket.com.au</li>
      <li>thebrightsocket.com.au</li>
    </ul>
    <div class="divider"></div>
    <p class="tagline"><span class="tagline__hours">24/7</span> Sydney Electrician</p>
  </section>

  <section class="card card--logo" aria-label="Logo side">
    <div class="texture" role="img" aria-label="Faint embossed repeat of the company name across the card"></div>
    <div class="wordmark">The Bright<br>Socket</div>
    <div class="social-links" aria-label="Social media">
      <span></span><span></span><span></span>
    </div>
  </section>
</body>
</html>
```